Real estate investor business card to retire young ;)!

I need a logo design and a business card. I am based in Montreal, Canada. I buy multi-family properties and do lots development. The final design should communicate that I am a problem solver and reliable.

This card will be given to other investors, to potential sellers and industry experts.

Target Market(s)

Real estate community, multi-family owners

Industry/Entity Type

Real Estate Development

Contact Information for Business Card

My name: Karine Beaulac
email: immo.karine.beaulac@postelune.ca
cellphone: (438) 555-2947

Logo Text

Gestion immobilière

Font styles to use
Sans Serif

Colors
3176b5

Requirements
Must have
• Within 1-2 seconds the person who sees my card should know that I buy properties and lot. Areas to for Phone number and email adress. I do not have a business name. The card should simply state my name and what I do. The logo should be remembered by the person who reads my card
Should not have
• Colors too bright. Too much small details. I want something balanced, bold without being agressive.

```html
<!DOCTYPE html>
<html lang="en">
<head>
<meta charset="utf-8">
<title>Karine Beaulac — Business Card</title>
<link href="https://fonts.googleapis.com/css2?family=Lexend:wght@400;700&family=Mulish:wght@400;600&display=swap" rel="stylesheet">
<style>
  :root {
    --backdrop: #cfcfcf;
    --card: #050505;
    --name-grey: #a4a4a6;
    --brand-blue: #3176b5;
    --text-light: #e6e6e6;
  }
  * { box-sizing: border-box; margin: 0; padding: 0; }
  html, body {
    width: 1200px;
    height: 1000px;
    overflow: hidden;
    background: var(--backdrop);
  }
  .sheet {
    position: relative;
    width: 1200px;
    height: 1000px;
    display: flex;
    align-items: center;
    justify-content: center;
    gap: 60px;
  }
  .card {
    position: relative;
    width: 520px;
    height: 300px;
    background: var(--card);
    border-radius: 4px;
    box-shadow: 0 10px 24px rgba(0,0,0,0.25);
    overflow: hidden;
  }

  /* Back side: identity */
  .card--identity {
    display: flex;
    flex-direction: column;
    justify-content: center;
    padding-left: 70px;
  }
  .identity__mark {
    display: flex;
    align-items: center;
    gap: 16px;
  }
  .identity__dot {
    width: 54px;
    height: 54px;
    border-radius: 50%;
    background: var(--brand-blue);
    flex: none;
  }
  .identity__name {
    font-family: "Lexend", sans-serif;
    font-weight: 700;
    font-size: 32px;
    line-height: 1.05;
    color: var(--brand-blue);
  }
  .identity__tagline {
    margin-top: 18px;
    font-family: "Mulish", sans-serif;
    font-weight: 400;
    font-size: 15px;
    color: var(--text-light);
    letter-spacing: 0.02em;
  }

  /* Front side: contact */
  .card--contact {
    padding: 44px 0 0 52px;
  }
  .contact__first {
    font-family: "Lexend", sans-serif;
    font-weight: 700;
    font-size: 92px;
    line-height: 0.9;
    color: var(--name-grey);
    letter-spacing: 0.01em;
  }
  .contact__last {
    font-family: "Lexend", sans-serif;
    font-weight: 700;
    font-size: 50px;
    line-height: 1;
    color: var(--brand-blue);
    margin-top: 2px;
    margin-left: 30px;
  }
  .contact__details {
    list-style: none;
    margin-top: 22px;
    margin-left: 64px;
    font-family: "Mulish", sans-serif;
    font-size: 15px;
    color: var(--text-light);
  }
  .contact__details li {
    display: flex;
    align-items: center;
    gap: 10px;
    line-height: 1.45;
  }
  .contact__icon {
    width: 13px;
    height: 13px;
    fill: var(--brand-blue);
    flex: none;
  }
</style>
</head>
<body>
  <main class="sheet">
    <section class="card card--identity" aria-label="Card back">
      <div class="identity__mark">
        <span class="identity__dot"></span>
        <span class="identity__name">Gestion<br>immobilière</span>
      </div>
      <p class="identity__tagline">Buy multi-family properties and development</p>
    </section>

    <section class="card card--contact" aria-label="Card front">
      <h1 class="contact__first">KARINE</h1>
      <h2 class="contact__last">BEAULAC</h2>
      <ul class="contact__details">
        <li>
          <svg class="contact__icon" viewBox="0 0 16 16" aria-hidden="true">
            <path d="M1 6 L8 1 L15 6 V15 H1 Z M1 6 L8 10 L15 6"/>
          </svg>
          immo.karine.beaulac@postelune.ca
        </li>
        <li>
          <svg class="contact__icon" viewBox="0 0 16 16" aria-hidden="true">
            <path d="M3 1 L6 1 L7 5 L5 6.5 C6 9 7 10 9.5 11 L11 9 L15 10 V13 C15 14 14 15 13 15 C6 14 2 10 1 3 C1 2 2 1 3 1 Z"/>
          </svg>
          (438) 555-2947
        </li>
      </ul>
    </section>
  </main>
</body>
</html>
```